TELVORIQ HOA Portal Site for Public

Clean up and organize current website; need website to look good and functional; this is a HOA (homeowner association management) website where homeowners can login and pay their bill, general information about a HOA, monthly newsletter page.
Competitors:
https://plumbrivet.com/
https://duskorrahill.com/
https://www.qxlivingspan.com/nevada
http://www.bpt-hoa.com/

Target Market(s)

homeowners

Industry/Entity Type

Real Estate

Coding

Coded - Design and coding required

Number of Pages Required

5+ page

Font styles to use
Serif

Colors
0292cd
33a6d7
e667a6
e34297

Requirements
Must have
• login to pay
• services page
• contact us
• order resale package
Nice to have
• page why an HOA would contract us

```html
<!DOCTYPE html>
<html lang="en">
<head>
<meta charset="utf-8">
<title>Telvoriq – Homeowner association management</title>
<link rel="stylesheet" href="https://fonts.googleapis.com/css2?family=Noto+Sans:wght@400;600&family=Tinos:wght@700&display=swap">
<style>
  :root {
    --topbar-blue: #0070f3;
    --header-grey: #7a7f85;
    --text-dark: #212529;
    --text-muted-nav: #3a3f44;
    --hero-title: #b9ecef;
    --white: #ffffff;
    --content-bg: #f8f9fa;
    --rule: #dee2e6;
    --accent-red: #e0344a;
    --hero-sky: #7f86c4;
    --hero-house: #c9c6d6;
    --hero-green: #2f5a2e;
    --hero-pool: #3fb7c4;
  }
  * { box-sizing: border-box; margin: 0; padding: 0; }
  html, body { width: 1020px; height: 1200px; overflow: hidden; }
  body {
    font-family: "Noto Sans", Arial, sans-serif;
    color: var(--text-dark);
    background: var(--white);
    font-size: 13.5px;
  }
  .topbar {
    height: 74px;
    background: var(--topbar-blue);
    position: relative;
  }
  .topbar__contact {
    position: absolute; left: 15px; top: 16px;
    font-family: "Tinos", "Times New Roman", serif;
    font-weight: 700; font-size: 14.5px; color: var(--text-dark);
    display: flex; align-items: center; gap: 4px;
  }
  .topbar__contact svg { width: 13px; height: 13px; }
  .topbar__tagline {
    position: absolute; left: 608px; top: 16px; font-size: 13.5px;
  }
  .topbar__login {
    position: absolute; right: 16px; top: 16px;
    padding: 4px 8px; font-size: 14.5px;
    border-right: 2px solid var(--accent-red);
    border-bottom: 2px solid var(--accent-red);
    color: var(--text-dark); text-decoration: none;
  }
  .site-header {
    height: 104px; background: var(--header-grey); position: relative;
  }
  .brand { position: absolute; left: 15px; top: 14px; }
  .brand__name { font-size: 34px; font-weight: 600; line-height: 1.2; }
  .brand__tag { font-size: 17px; margin-top: 4px; }
  .main-nav {
    position: absolute; right: 20px; top: 42px;
    display: flex; gap: 14px; font-size: 13.5px;
  }
  .main-nav a { color: var(--text-muted-nav); text-decoration: none; }
  .main-nav a.is-active { color: var(--text-dark); }
  .hero {
    height: 578px; position: relative;
    background:
      linear-gradient(180deg, transparent 0%, transparent 70%, rgba(47,90,46,.9) 82%, var(--hero-pool) 95%),
      linear-gradient(100deg, var(--hero-green) 0%, #6d5f8f 30%, var(--hero-sky) 45%, var(--hero-house) 70%, #8c8aa2 100%);
  }
  .hero__text { position: absolute; left: 153px; top: 302px; }
  .hero__title { font-size: 36px; font-weight: 600; color: var(--hero-title); }
  .hero__sub { font-size: 16px; color: var(--white); margin-top: 18px; }
  .content {
    background: var(--content-bg); padding: 20px 2px 38px; height: 368px;
  }
  .content h2 {
    font-size: 20px; font-weight: 400; line-height: 1.27;
    text-transform: uppercase; margin-bottom: 8px;
  }
  .content p { line-height: 1.6; }
  .content ol { margin: 16px 0 16px 38px; line-height: 1.6; }
  .site-footer {
    border-top: 1px solid var(--rule);
    height: 76px; position: relative; background: var(--white);
  }
  .site-footer__copy {
    position: absolute; left: 23px; top: 24px; font-size: 13.5px; text-transform: uppercase;
  }
  .social { position: absolute; left: 776px; top: 26px; display: flex; gap: 19px; align-items: center; }
  .social__mark { width: 13px; height: 13px; background: var(--text-dark); border-radius: 2px; }
  .social svg { width: 14px; height: 14px; }
</style>
</head>
<body>
  <div class="topbar">
    <div class="topbar__contact">
      <svg viewBox="0 0 16 16" aria-hidden="true"><circle cx="8" cy="8" r="7" fill="none" stroke="#212529" stroke-width="2"/><circle cx="8" cy="8" r="2.5" fill="#212529"/></svg>
      000 123 456 789
      <svg viewBox="0 0 16 12" aria-hidden="true" style="width:14px;margin-left:4px"><rect x="0" y="0" width="16" height="12" rx="1" fill="#212529"/><path d="M0 1 L8 7 L16 1" stroke="#0070f3" stroke-width="1.4" fill="none"/></svg>
      NAME@EMAIL.COM
    </div>
    <div class="topbar__tagline">Lets work together</div>
    <a class="topbar__login" href="#">Homeowner log-in</a>
  </div>

  <header class="site-header">
    <div class="brand">
      <div class="brand__name">Telvoriq</div>
      <div class="brand__tag">Homeowner association management</div>
    </div>
    <nav class="main-nav">
      <a href="#">Homeowner</a>
      <a href="#">Services</a>
      <a href="#">Contact us</a>
      <a href="#" class="is-active">order resale package</a>
    </nav>
  </header>

  <section class="hero" role="img" aria-label="Photo of a modern two-storey villa with tropical garden and pool at dusk">
    <div class="hero__text">
      <h1 class="hero__title">Great service you matter</h1>
      <p class="hero__sub">We are here to help</p>
    </div>
  </section>

  <main class="content">
    <h2>To obtain or order a resale package, resale demand, association questionnaire, HOA financial data, or governing documents for your home or association – must register first (see above):</h2>
    <p>As a homeowner in an Association managed by TELVORIQ, you have 24-hour access to your account. You can view your balance and payment history, retrieve and fill out forms, and much more. Note: address changes should be submitted to coa@duskorrahill.com. If you are trying to make a payment or set up auto pay please visit the “Pay Assessments” page. You can also set up auto pay by emailing accounting@duskorrahill.com for an ACH form</p>
    <ol>
      <li>Lorem ipsum dolor sit amet, consectetur adipisicing elit. Consequatur, inventore.</li>
      <li>Lorem ipsum dolor sit amet, consectetur adipisicing elit. Consequatur, inventore.</li>
      <li>Lorem ipsum dolor sit amet, consectetur adipisicing elit. Consequatur, inventore.</li>
    </ol>
    <p>Lorem ipsum dolor sit amet, consectetur adipisicing elit. Molestiae quas illo architecto minus aspernatur reprehenderit eaque temporibus amet. Velit a repellat sed saepe nam vero, totam sint harum tenetur libero praesentium voluptas ad rerum culpa cumque amet autem, quam illo eveniet esse consectetur molestiae architecto. Minima magni, libero soluta odio.</p>
  </main>

  <footer class="site-footer">
    <div class="site-footer__copy">Copyright 2019 Telvoriq. | All rights reserved</div>
    <div class="social">
      <span class="social__mark" aria-label="Social profile"></span>
      <span class="social__mark" aria-label="Social profile"></span>
      <svg viewBox="0 0 16 16" aria-label="Phone"><path d="M3 1 L6 1 L7 5 L5 6.5 C6 9 7 10 9.5 11 L11 9 L15 10 L15 13 C15 14 14 15 13 15 C6 15 1 10 1 3 C1 2 2 1 3 1 Z" fill="#212529"/></svg>
      <span class="social__mark" aria-label="Social profile"></span>
    </div>
  </footer>
</body>
</html>
```